Wheelcraft forum banner

Need a banner ad for a forum relating to the motor car industry.
I have attached a sample banner , we need ours to be edited to suit our web site - wheelcraft.com.au
Image needs to be roughly 400px by 100px.
We would like to display information like the pic below named kelbanner but with a better design / colour / image combination.

```html
<!DOCTYPE html>
<html lang="en">
<head>
<meta charset="utf-8">
<title>Wheelcraft forum banner</title>
<link href="https://fonts.googleapis.com/css2?family=Roboto+Condensed:ital,wght@0,400;0,700;1,800&display=swap" rel="stylesheet">
<style>
  :root {
    --page: #ffffff;
    --banner-dark: #262322;
    --streak-red: #8a1a12;
    --streak-orange: #c8521c;
    --streak-glow: #e9a34a;
    --car-grey: #6d6f74;
    --car-red: #8e1424;
    --text-light: #ffffff;
    --text-muted: #d9d9d9;
  }
  html, body {
    margin: 0;
    padding: 0;
    width: 1000px;
    height: 1200px;
    overflow: hidden;
    background: var(--page);
  }
  .canvas {
    position: relative;
    width: 1000px;
    height: 1200px;
  }
  .forum-banner {
    position: absolute;
    left: 300px;
    top: 424px;
    width: 400px;
    height: 100px;
    overflow: hidden;
    background: var(--banner-dark);
    font-family: "Roboto Condensed", "Arial Narrow", sans-serif;
  }
  .banner-backdrop {
    position: absolute;
    inset: 0;
    background:
      radial-gradient(ellipse 120px 30px at 150px 8px, var(--streak-glow) 0%, rgba(233,163,74,0) 100%),
      linear-gradient(168deg, var(--streak-red) 0%, var(--streak-orange) 18%, rgba(138,26,18,0.6) 34%, rgba(38,35,34,0) 55%),
      linear-gradient(180deg, #3a2a26 0%, var(--banner-dark) 70%);
  }
  .vehicle-photo {
    position: absolute;
    right: 0;
    top: 4px;
    width: 186px;
    height: 96px;
    background: linear-gradient(100deg, var(--car-grey) 0%, #4a4b50 38%, var(--car-red) 62%, #5e0c18 100%);
  }
  .brand {
    position: absolute;
    left: 13px;
    top: 9px;
    display: flex;
    align-items: center;
    gap: 4px;
  }
  .brand-mark {
    width: 8px;
    height: 8px;
    background: var(--text-light);
  }
  .brand-name {
    font-size: 17px;
    font-weight: 700;
    letter-spacing: 0.5px;
    color: var(--text-light);
    line-height: 1;
  }
  .brand-tagline {
    position: absolute;
    left: 14px;
    top: 29px;
    font-size: 4.5px;
    letter-spacing: 0.4px;
    color: var(--text-muted);
    text-transform: uppercase;
  }
  .service-title {
    position: absolute;
    left: 12px;
    top: 43px;
    margin: 0;
    font-size: 15px;
    font-weight: 400;
    color: var(--text-light);
    letter-spacing: 0.1px;
  }
  .service-detail {
    position: absolute;
    left: 12px;
    top: 66px;
    margin: 0;
    font-size: 11.5px;
    line-height: 12px;
    color: var(--text-light);
  }
  .service-detail span { display: block; }
  .service-detail .lead { padding-left: 1px; }
</style>
</head>
<body>
<main class="canvas">
  <section class="forum-banner" aria-label="Wheelcraft Japan car import service banner">
    <div class="banner-backdrop" role="img" aria-label="Dark background with red and orange light streaks"></div>
    <div class="vehicle-photo" role="img" aria-label="Photo of a silver hatchback and a red minivan, front three-quarter view"></div>
    <div class="brand">
      <span class="brand-mark"></span>
      <span class="brand-name">WHEELCRAFT</span>
    </div>
    <div class="brand-tagline">Quality Japanese vehicle imports</div>
    <h1 class="service-title">JAPAN CAR IMPORT SERVICE</h1>
    <p class="service-detail">
      <span class="lead">We arrange everything for you</span>
      <span>(Vehicel purchase, shipping, costoms, compliance)</span>
    </p>
  </section>
</main>
</body>
</html>
```